Newsletter-Design für Garten-Samen Shop
Zielgruppe
Online Shop für Obst-, Gemüse-, Kräuter- und Pflanzensamen
Aufgabenstellung
www.beetfreunde-portal.example ist die Seite mit den Produkten. Als Tipp sollte das Jiaogulan genannt werden da dieses Produkt sich am meisten verkauft.

```html
<!DOCTYPE html>
<html lang="de">
<head>
<meta charset="utf-8">
<title>Garten Tipps – Newsletter</title>
<link rel="stylesheet" href="https://fonts.googleapis.com/css2?family=Lato:wght@400;700;900&family=Roboto+Condensed:wght@700&display=swap">
<style>
:root{
  --purple:#955a8f;
  --red:#e94b4b;
  --ink:#1e1e1e;
  --text:#222;
  --muted:#666;
  --line:#bdbdbd;
  --soft:#f1f1f1;
  --white:#fff;
}
*{margin:0;padding:0;box-sizing:border-box}
html,body{width:1200px;height:2571px;overflow:hidden;background:var(--white)}
body{position:relative;font-family:Arial,Helvetica,sans-serif;color:var(--text)}
.abs{position:absolute}
.newsletter{position:absolute;left:236px;top:0;width:730px;background:var(--white);box-shadow:0 0 3px rgba(0,0,0,.08)}
.header{position:absolute;left:0;top:0;width:730px;height:82px;background:linear-gradient(#fff,#f7f7f7)}
.brand{position:absolute;left:107px;top:8px;font-family:Lato,sans-serif;font-weight:900;font-size:34px;color:var(--ink);letter-spacing:-.3px}
.tagline{position:absolute;left:107px;top:54px;font-family:Lato,sans-serif;font-size:15px;color:var(--ink)}
.social{position:absolute;right:108px;top:33px;display:flex;gap:10px;font-family:Lato,sans-serif;font-size:11px;color:#aaa}
.hero{position:absolute;left:0;top:82px;width:730px;height:273px;background:linear-gradient(100deg,#3f7a2c 0%,#e0823a 28%,#c83a2f 45%,#b99a5d 62%,#e6a02a 78%,#5d8f2e 100%)}
.hero-band{position:absolute;left:0;bottom:0;width:730px;height:83px;background:rgba(0,0,0,.28)}
.hero-title{position:absolute;left:107px;top:204px;font-family:Lato,sans-serif;font-weight:900;font-size:23px;line-height:29px;color:#fff}
.content{position:absolute;left:107px;width:516px}
.greeting{top:390px;font-size:20px;font-weight:bold;color:var(--ink)}
.copy{font-size:14px;line-height:18px;color:var(--text);letter-spacing:-.15px}
.section-head{height:37px;border-top:1px solid var(--line);border-bottom:1px solid var(--line);text-align:center;font-family:Lato,sans-serif;font-size:18px;line-height:36px;letter-spacing:.8px;color:#444}
.tip-title{position:absolute;left:77px;width:576px;top:692px;text-align:center;white-space:nowrap;font-size:29px;line-height:34px;font-weight:bold;color:var(--purple)}
.tip-image{top:735px;height:343px;background:linear-gradient(#f4f8f4 0%,#5aa344 12%,#2f7a25 55%,#1f5a1a 100%)}
.badge{position:absolute;left:389px;top:17px;width:106px;height:106px;border-radius:50%;background:var(--purple);color:#fff;font-family:"Roboto Condensed",sans-serif;font-weight:700;font-size:17px;display:flex;align-items:center;justify-content:center}
.btn{position:absolute;background:var(--purple);color:#fff;font-family:Lato,sans-serif;font-weight:700;text-align:center}
.btn-read{left:295px;top:1224px;width:147px;height:42px;font-size:17px;line-height:42px}
.card{position:absolute;width:239px;border:3px solid #f1f1f1;background:#fff}
.card-img{position:absolute;left:0;top:0;width:233px;height:233px}
.card-name{position:absolute;left:0;width:233px;text-align:center;font-family:Lato,sans-serif;font-size:14px;letter-spacing:.6px;color:#555;white-space:nowrap}
.card-price{position:absolute;left:0;width:233px;text-align:center;font-family:Lato,sans-serif;font-weight:700;font-size:16px;color:#555}
.card-price s{color:#aaa;margin-right:6px}
.btn-offer{left:57px;width:123px;height:33px;font-size:13px;line-height:33px}
.ribbon{position:absolute;left:-3px;top:24px;width:68px;height:30px;background:var(--red);color:#fff;font-family:Lato,sans-serif;font-size:11px;line-height:30px;text-align:center;letter-spacing:.3px}
.service{position:absolute;left:0;top:2234px;width:730px;height:136px;background:var(--purple)}
.agent{position:absolute;left:486px;top:2150px;width:136px;height:220px;border-radius:68px 68px 0 0;background:linear-gradient(#b89ad0,#9a6fbf)}
.service-text{position:absolute;left:106px;top:2258px;z-index:2;white-space:nowrap;font-family:Lato,sans-serif;font-size:15.5px;line-height:19px;color:#fff}
.service-phone{position:absolute;left:120px;top:2308px;z-index:2;display:flex;align-items:center;gap:8px;font-family:Lato,sans-serif;font-weight:900;font-size:33px;color:#fff}
.footer{position:absolute;left:0;top:2370px;width:1200px;height:201px;background:var(--soft)}
.foot-col{position:absolute;top:35px;font-family:Lato,sans-serif;font-size:10px;line-height:17px;color:#888}
.unsub{position:absolute;left:0;top:166px;width:1200px;text-align:center;font-family:Lato,sans-serif;font-size:10px;color:#888;text-decoration:underline}
</style>
</head>
<body>
<div class="footer">
  <div class="foot-col" style="left:345px">Beetwerk Versand GmbH<br>diese vertreten<br>durch den Geschäftsführer<br>Jonas Vehrenkamp</div>
  <div class="foot-col" style="left:506px">Lindenallee 12<br>31999 Grünfeld<br>Deutschland<br>Telefon: 0555 0123 4567<br>Telefax: 0555 0123 4568<br>E-Mail: service@beetfreunde-portal.example</div>
  <div class="foot-col" style="left:658px">USt-IdNr.: DE000123456<br>eingetragen im Handelsregister<br>des Amtsgerichtes Amtsgericht Musterstadt<br>Handelsregisternummer HRB HRB 1029</div>
  <div class="unsub">Newsletter abbestellen</div>
</div>

<div class="newsletter" style="height:2370px">
  <header class="header">
    <div class="brand">Garten Tipps</div>
    <div class="tagline">Obst, Gemüse + Pflanzen</div>
    <div class="social"><span>Kreis</span><span>Treff</span><span>Ruf</span></div>
  </header>

  <div class="hero" role="img" aria-label="Foto: bunte Auswahl an frischem Obst und Gemüse">
    <div class="hero-band"></div>
    <div class="hero-title">Obst-, Gemüse-, Pflanzen- und Kräuter-Samen<br>aus dem eigenen Garten</div>
  </div>

  <div class="content abs greeting">Lieber Leser,</div>
  <p class="content abs copy" style="top:433px">Obst und Gemüse aus dem eigenen Garten ist immer toll, denn da weiß man was auf den Teller kommt. Zudem schmeckt es frisch aus dem Garten ohnehin besser als aus dem Supermarkt. Wer Kinder hat, kann Obst und Gemüse zusammen mit den Kindern pflanzen. Die Kleinen sehen dann die Erfolge und lernen Pflanzen auch als Lebewesen kennen, die wachsen.</p>
  <p class="content abs copy" style="top:541px">Viele schreckt jedoch der eigene Anbau ab, weil man denkt das der Aufwand hierfür zu groß ist. Dabei muss ein Obst- und Gemüsebeet gar nicht viel Arbeit machen und riesig sein muss es auch nicht.</p>

  <div class="content abs section-head" style="top:630px">UNSER TIPP</div>
  <h2 class="tip-title">Jiaogulan – Kraut der Unsterblichkeit</h2>
  <div class="content abs tip-image" role="img" aria-label="Foto: dichte grüne Jiaogulan-Ranken">
    <div class="badge">BESTSELLER</div>
  </div>
  <p class="content abs copy" style="top:1103px">Das stark rankend Kraut der Unsterblichkeit stammt aus China und Japan. Als Su­perfood erlangte Jiaogulan in den letzten Jahren auch in der westlichen Welt zune­hmend an Bedeutung. Jiaogulan – so fanden Forscher verschiedener Universitäten heraus – verbessert die Nährstoff-Versorgung aller Organe, die Herzleistung und die Blutzirkulation. Auch auf das Hormonsystem und das zentrale Nervensystem hat es positive Wirkung.</p>
  <div class="btn btn-read">WEITER LESEN</div>

  <div class="content abs section-head" style="top:1306px">BELIEBTE PRODUKTE</div>

  <div class="card" style="left:108px;top:1385px;height:351px">
    <div class="card-img" role="img" aria-label="Foto: Bambuswald" style="background:linear-gradient(90deg,#6f9f88,#a9cbb4,#5f8d78,#9cc2ab,#6f9f88)"></div>
    <div class="card-name" style="top:248px">CHINESISCHER RIESENBAMBUS</div>
    <div class="card-price" style="top:272px">6,95 €</div>
    <div class="btn btn-offer" style="top:302px">ZUM ANGEBOT</div>
  </div>

  <div class="card" style="left:383px;top:1385px;height:351px">
    <div class="card-img" role="img" aria-label="Foto: roter Ahornbaum im Park" style="background:linear-gradient(#e8eef2 0%,#e0304a 30%,#d8253f 65%,#5b9a3b 85%,#6aa844 100%)"></div>
    <div class="ribbon">ANGEBOT</div>
    <div class="card-name" style="top:248px">JAPANISCHER ROTER AHORN</div>
    <div class="card-price" style="top:272px"><s>9,99 €</s>8,89 €</div>
    <div class="btn btn-offer" style="top:302px">ZUM ANGEBOT</div>
  </div>

  <div class="card" style="left:108px;top:1775px;height:346px">
    <div class="card-img" role="img" aria-label="Foto: Mandarinenbaum mit reifen Früchten" style="height:223px;background:radial-gradient(circle at 45% 55%,#f08a1c 0%,#d9701a 35%,#3f6a2a 70%,#7fa3cf 100%)"></div>
    <div class="ribbon">ANGEBOT</div>
    <div class="card-name" style="top:246px">MANDARINENBAUM</div>
    <div class="card-price" style="top:268px"><s>7,99 €</s>6,99 €</div>
    <div class="btn btn-offer" style="top:297px">ZUM ANGEBOT</div>
  </div>

  <div class="card" style="left:383px;top:1775px;height:346px">
    <div class="card-img" role="img" aria-label="Foto: lila blühender Palisanderbaum" style="height:223px;background:linear-gradient(135deg,#8b7cc8,#b1a2e0,#7c6bb8,#a897da)"></div>
    <div class="card-name" style="top:246px">PALISANDERBAUM</div>
    <div class="card-price" style="top:270px">4,99 €</div>
    <div class="btn btn-offer" style="top:297px">ZUM ANGEBOT</div>
  </div>

  <div class="service"></div>
  <div class="agent" role="img" aria-label="Foto: Kundenberaterin mit Headset"></div>
  <div class="service-text">Sie haben Fragen oder benötigen mehr Informationen?<br>Unser Kundenservice hilft Ihnen weiter:</div>
  <div class="service-phone">
    <svg width="28" height="28" viewBox="0 0 24 24" aria-hidden="true"><path fill="#fff" d="M6.6 10.8a15.1 15.1 0 0 0 6.6 6.6l2.2-2.2a1 1 0 0 1 1-.25 11.4 11.4 0 0 0 3.6.57 1 1 0 0 1 1 1V20a1 1 0 0 1-1 1A17 17 0 0 1 3 4a1 1 0 0 1 1-1h3.5a1 1 0 0 1 1 1c0 1.25.2 2.45.57 3.57a1 1 0 0 1-.25 1z"/></svg>
    <span>0555 0123 4567</span>
  </div>
</div>
</body>
</html>
```